120ml Jar Label — Masculine Cosmetic Foot Balm for Cracked, Hardworking Heels

We need a print-ready wraparound label for a 120ml jar — a brown/amber glass jar with a black metal screw lid (file photo attached).

--DO NOT PUT A BARCODE ON THE LABEL PLEASE--
**PLEASE READ "PLAN HUDDLE PROJECT BRIEF FINAL.MD" IN ATTACHED FILES IF YOU ARE SUBMITTING A DESIGN.**

The label is 190mm wide × 40mm high.
We need files to be in an .ai format with a 2mm bleed at the end.
Social media handle: @bramblekeepnz (facebook, instagram and tiktok)

Bramble Keep is a New Zealand foot-care brand making practical, no-nonsense products for hardworking men whose jobs wreck their feet. Our flagship product, Ridge Mender Balm, helps fix thick, cracked, hardworking skin.

Brand color scheme and overview is all in the brief file. You may add some brand aligned colors outside of the specified hex codes as you see fit to make a great design. Feel free to remove the "Bramble Keep" text from the logo so Bramble Keep is not doubled up on the front of the label

The tone we want: direct, rugged, and credible — like a workwear brand, not a spa brand. Most cracked-heel products on the market lean soft and feminine; we want to stand apart by looking like a serious fix for a real problem, made in New Zealand.

Full legal requirements for New Zealand cosmetic labelling (ingredients, directions, net contents, origin, etc.) are listed in the attached brief document — these are non-negotiable and must stay legible.

Please see the label attached "Label spacing guide" for this project's rough spacing guide. This label is the same size and sits well on the jar. This label doesn't need to be spaced quite as much as the Verin Label

I want to run the design for a week - I feel 7 days is a good amount of time for designers to see the work, digest the brief and create something remarkable and memorable for Bramble Keep.

Target Market(s)

Working men in New Zealand whose jobs or lifestyle put heavy wear on their feet — tradies, farmers, hospital/shift workers, hunters, and outdoors people. Practical, value-driven buyers rather than luxury skincare shoppers.

Industry/Entity Type

Beauty / Health & Wellness / Cosmetics

Font styles to use
Sans Serif
Other font styles liked:
• Montserrat (bold, headings), Inter (regular, body)

Colors
00AB8E
00BBA5
67D7C9
C6EFE9
E9F9F6
FFC000
F8CF3A
FAE287
FDF2CF
FEFAEE

Requirements
Must have
• All NZ cosmetic labelling requirements from the attached brief (product name, tag line, net contents, ingredients, directions, storage, made in NZ) — legible and complete, not omitted for aesthetics Fits 190mm × 40mm wraparound format for a 120ml brown jar with black lid Uses our existing brand colors: Deep Olive #3C4A34, Bone White #F4EFE6, Terracotta Clay #C1683D, and Warm Grey #4A4540 (exact palette in attached brief) Uses Montserrat (headings) and Inter (body) or close equivalents Incorporates our existing shield-and-wing logo (attached) Brand name and product name clearly readable from a normal shelf/bathroom-cabinet distance
Nice to have
• A style that could extend into a hero/product photo later, similar to the NZ-hills-backdrop look on our website (screenshot attached) — not required for the label itself, just good to keep in mind Original icon work (e.g. a small soak/apply/sock icon set) if it fits the rugged brand feel A design that could work as a small back-label/wraparound split if the front can't fit everything at a readable size
Should not have
• No pastel colors, floral motifs, or delicate script fonts — this should never look like spa/luxury skincare. Don't introduce new brand colors outside the palette provided other than black.

```html
<!DOCTYPE html>
<html lang="en">
<head>
<meta charset="utf-8">
<title>Bramble Keep — Ridge Mender Balm Label</title>
<link href="https://fonts.googleapis.com/css2?family=Inter:wght@400;500;600&family=Montserrat:wght@500;700&family=Oswald:wght@600&display=swap" rel="stylesheet">
<style>
  :root {
    --backdrop: #e4e4e4;
    --olive-deep: #2f3e32;
    --clay-frame: #8b5a31;
    --clay-accent: #b8743c;
    --bone: #f1e9da;
    --bone-soft: #e6dfd2;
    --muted: #9c8a73;
  }
  * { box-sizing: border-box; margin: 0; padding: 0; }
  html, body { width: 1200px; height: 912px; overflow: hidden; }
  body {
    background: var(--backdrop);
    font-family: "Inter", Arial, sans-serif;
    position: relative;
  }
  .label {
    position: absolute;
    left: 40px; top: 338px;
    width: 1120px; height: 236px;
    background: var(--clay-frame);
    border-radius: 14px;
    padding: 7px;
  }
  .label-face {
    position: relative;
    width: 100%; height: 100%;
    background: var(--olive-deep);
    border-radius: 9px;
    color: var(--bone);
  }
  .panel { position: absolute; }

  /* back panel */
  .back-panel { left: 24px; top: 18px; width: 280px; height: 200px; }
  .info-block { font-size: 12.4px; line-height: 14.4px; color: var(--bone-soft); }
  .info-block .lead { color: var(--clay-accent); font-weight: 500; }
  .divider { height: 1px; background: var(--clay-accent); opacity: .55; margin: 14px 0 13px; }
  .distributor { margin-top: 14px; font-size: 12.4px; line-height: 16px; color: var(--muted); }
  .distributor .name, .distributor .web strong { color: var(--clay-accent); font-weight: 600; }
  .social-row {
    position: absolute; left: 140px; top: 176px;
    display: flex; align-items: center; gap: 18px;
  }
  .social-handle {
    font-size: 12px; line-height: 14px; font-weight: 600; color: var(--bone);
    white-space: nowrap;
  }
  .care-marks { display: flex; gap: 6px; }
  .care-mark { width: 20px; height: 20px; border: 1.5px solid var(--bone); border-radius: 4px; }
  .care-mark.round { border-radius: 50%; }

  /* front panel */
  .front-panel { left: 380px; top: 14px; width: 360px; text-align: center; }
  .brand-lockup { display: flex; align-items: center; justify-content: center; gap: 12px; }
  .brand-mark { width: 44px; height: 44px; border-radius: 50%; background: var(--clay-accent); }
  .brand-name {
    font-family: "Oswald", "Arial Narrow", sans-serif;
    font-weight: 600; font-size: 31px; line-height: 32px;
    letter-spacing: .5px; color: var(--bone); text-transform: uppercase;
  }
  .brand-name small { display: block; font-size: 18px; line-height: 18px; }
  .product-name {
    margin-top: 10px;
    font-family: "Montserrat", Arial, sans-serif;
    font-weight: 700; font-size: 37px; line-height: 38px;
    color: var(--bone); text-transform: uppercase;
  }
  .tagline {
    display: inline-block; margin-top: 8px;
    border: 1.5px solid var(--clay-accent); border-radius: 10px;
    padding: 1px 11px;
    font-family: "Montserrat", Arial, sans-serif; font-weight: 500;
    font-size: 12.5px; color: var(--bone);
  }
  .net-contents {
    position: absolute; left: 409px; top: 208px;
    font-family: "Montserrat", Arial, sans-serif; font-size: 10.5px; color: var(--bone);
  }
  .origin-badge {
    position: absolute; left: 671px; top: 192px;
    width: 78px; height: 26px;
    border: 1.5px solid var(--bone);
    font-family: "Montserrat", Arial, sans-serif; font-weight: 700;
    color: var(--bone); text-align: center; line-height: 1;
  }
  .origin-badge .top { display: block; font-size: 11px; padding-top: 2px; }
  .origin-badge .bottom {
    display: block; margin-top: 2px; font-size: 7px; letter-spacing: 1px;
    border-top: 1.5px solid var(--bone); padding-top: 1px;
  }

  /* directions panel */
  .directions-panel { left: 822px; top: 10px; width: 270px; }
  .directions-title {
    margin-left: 86px;
    font-family: "Inter", Arial, sans-serif; font-weight: 600;
    font-size: 14px; color: var(--clay-accent);
  }
  .step { display: flex; align-items: center; gap: 17px; font-size: 12.4px; line-height: 14.4px; color: var(--bone); }
  .step-icon { flex: none; width: 38px; height: 38px; }
  .step-icon.flat { border-radius: 8px; background: linear-gradient(160deg, #8b5a31, #5e4530); }
  .step:nth-child(2) { margin-top: 2px; }
  .step:nth-child(3) { margin-top: 8px; }
  .step:nth-child(4) { margin-top: 12px; }
  .step:nth-child(5) { margin-top: 12px; }
</style>
</head>
<body>
  <div class="label">
    <div class="label-face">

      <section class="panel back-panel">
        <p class="info-block"><span class="lead">STORAGE:</span> Keep out of direct sunlight. Best used within six months of opening.</p>
        <div class="divider"></div>
        <p class="info-block"><span class="lead">INGREDIENTS:</span> Shea Butter, Beef Tallow, Beeswax, Grape Seed Oil, Vegetable Glycerin, Lanolin, Panthenol, Gluconolactone, Sodium Benzoate, Allantoin, Manuka Honey, Vitamin E, Tea Tree Essential Oil, Lemon Myrtle Essential Oil, Rosemary Oleoresin Extract.</p>
        <div class="distributor">
          <div>Distributed By:</div>
          <div class="name">Bramble Keep</div>
          <div class="web">www.<strong>bramblekeep</strong>.co</div>
        </div>
        <div class="social-row">
          <span class="social-handle">@bramblekeepnz</span>
          <div class="care-marks">
            <span class="care-mark round"></span>
            <span class="care-mark"></span>
          </div>
        </div>
      </section>

      <section class="panel front-panel">
        <div class="brand-lockup">
          <span class="brand-mark"></span>
          <div class="brand-name">Bramble Keep<small>NZ</small></div>
        </div>
        <h1 class="product-name">Ridge Mender<br>Balm</h1>
        <span class="tagline">For Hardworking Soles</span>
      </section>
      <span class="net-contents">40 oz / 120ml</span>
      <div class="origin-badge"><span class="top">MADE IN</span><span class="bottom">NEW ZEALAND</span></div>

      <section class="panel directions-panel">
        <h2 class="directions-title">DIRECTIONS:</h2>
        <div class="step">
          <svg class="step-icon" viewBox="0 0 38 38" aria-hidden="true">
            <ellipse cx="18" cy="11" rx="13" ry="4" fill="#f1e9da"/>
            <path d="M5 11v13c0 2.5 6 4.5 13 4.5s13-2 13-4.5V11" fill="#8b5a31" stroke="#f1e9da" stroke-width="1.2"/>
            <path d="M29 24c0 0-4 5-4 8a4 4 0 0 0 8 0c0-3-4-8-4-8z" fill="#b8743c"/>
          </svg>
          <span>Apply generously.</span>
        </div>
        <div class="step">
          <span class="step-icon flat" role="img" aria-label="Small icon of clean bare feet"></span>
          <span>To clean, dry feet, focusing on heels and thick or cracked areas.</span>
        </div>
        <div class="step">
          <span class="step-icon flat" role="img" aria-label="Small icon of socks under a crescent moon"></span>
          <span>For cracked heels, wear our moisture-locking socks overnight.</span>
        </div>
        <div class="step">
          <svg class="step-icon" viewBox="0 0 38 38" aria-hidden="true">
            <rect x="4" y="6" width="26" height="24" rx="3" fill="none" stroke="#b8743c" stroke-width="2"/>
            <line x1="4" y1="12" x2="30" y2="12" stroke="#b8743c" stroke-width="2"/>
            <line x1="10" y1="3" x2="10" y2="8" stroke="#b8743c" stroke-width="2"/>
            <line x1="24" y1="3" x2="24" y2="8" stroke="#b8743c" stroke-width="2"/>
            <g fill="#b8743c"><rect x="8" y="16" width="3" height="3"/><rect x="13" y="16" width="3" height="3"/><rect x="18" y="16" width="3" height="3"/><rect x="8" y="21" width="3" height="3"/><rect x="13" y="21" width="3" height="3"/></g>
            <circle cx="28" cy="29" r="7" fill="#b8743c"/>
            <path d="M25 29l2.2 2.2L31.5 27" fill="none" stroke="#2f3e32" stroke-width="1.8"/>
          </svg>
          <span>Use daily.</span>
        </div>
      </section>

    </div>
  </div>
</body>
</html>
```